Postcard Design hearing aid sales & service. Free hearing test . Fresh batteries

Bluebonnet Hearing Aid Device Center . Located at 417 Marwick Ln Abilene Texas 79488 Ph 325-555-0147.
Hours Mon thru Thurs 9:00am - 5:00pm closed for lunch 12:00pm - 1:00pm . Fri open 9:00am - 1:00pm
Hearing Test n/c Hearing aid adjustment & cleaning of hearing aids n/c . Fresh batteries buy one 1/2 off on 2nd pack. Limited time. Walk-in welcome Appointments appreciated. THIS MONTH ONLY Special discounts on new state of the art hearing aids w/remote. .

```html
<!DOCTYPE html>
<html lang="en">
<head>
<meta charset="utf-8">
<title>Bluebonnet Hearing Aid Device Center – Postcard</title>
<link href="https://fonts.googleapis.com/css2?family=Marcellus&family=Open+Sans:ital,wght@0,400;0,600;0,700;1,400&family=Oswald:wght@500&display=swap" rel="stylesheet">
<style>
  :root {
    --teal: #2f9fb0;
    --teal-light: #8fd3d6;
    --box: #d3ecee;
    --taupe: #b19c87;
    --brown: #6e4f33;
    --label: #a08a70;
    --ink: #2b2b2b;
    --grey: #666666;
    --paper: #ffffff;
    --backdrop: #ececec;
    --rule: #b5b5b5;
  }
  * { margin: 0; padding: 0; box-sizing: border-box; }
  html, body { width: 949px; height: 1200px; overflow: hidden; background: var(--backdrop); }
  body { position: relative; font-family: "Open Sans", Arial, sans-serif; color: var(--ink); }

  .card {
    position: absolute; width: 557px; height: 432px;
    background: var(--paper); overflow: hidden;
    transform: scale(1.2214); transform-origin: 0 0;
    box-shadow: 0 2px 6px rgba(0,0,0,.25);
  }
  .card--front { left: 85px; top: 49px; }
  .card--back  { left: 181px; top: 617px; }
  .card svg.shapes { position: absolute; inset: 0; }
  .txt { position: absolute; white-space: nowrap; }

  /* front */
  .hours { left: 20px; top: 14px; color: #fff; font-size: 8.6px; line-height: 11px; }
  .hours .head { font-size: 9px; margin-bottom: 3px; }
  .hours .small { font-size: 5.6px; line-height: 8px; }
  .title { font-family: "Marcellus", Georgia, serif; color: #fff; text-align: center; line-height: 1.08; }
  .front-title { left: 195px; width: 362px; top: 16px; font-size: 31px; }
  .tagline { font-weight: 700; color: var(--grey); font-size: 10.5px; line-height: 14px; text-align: center; }
  .front-tagline { left: 290px; width: 220px; top: 106px; }
  .service { left: 280px; width: 270px; top: 150px; font-size: 19px; text-align: center; color: var(--ink); }
  .free { left: 280px; width: 270px; top: 183px; font-size: 10.3px; font-weight: 600; text-align: center; color: #111; }

  .offer {
    position: absolute; top: 216px; width: 105px; height: 100px;
    background: var(--box); border-radius: 4px; text-align: center;
    box-shadow: 1px 2px 4px rgba(0,0,0,.18);
  }
  .offer--batteries { left: 320px; }
  .offer--discounts { left: 432px; }
  .offer .label { margin-top: 9px; font-size: 7.6px; font-weight: 700; color: var(--label); }
  .offer .deal { font-family: "Oswald", "Arial Narrow", sans-serif; font-weight: 500; color: var(--brown); font-size: 11.5px; line-height: 17px; margin-top: 15px; text-transform: uppercase; }
  .offer .note { font-size: 6.6px; font-weight: 700; color: var(--label); line-height: 10px; }
  .offer--batteries .note { margin-top: 14px; }
  .offer--discounts .note { color: var(--brown); }

  .welcome { font-style: italic; font-size: 9.8px; }
  .front-welcome { right: 40px; top: 336px; color: var(--grey); }
  .front-address { right: 40px; top: 353px; font-size: 10.8px; color: var(--ink); }
  .phone { color: #fff; font-weight: 700; display: flex; align-items: center; gap: 10px; }
  .phone svg { fill: #fff; }
  .front-phone { left: 365px; top: 390px; font-size: 19.5px; }

  /* back */
  .back-title { left: 0; width: 312px; top: 12px; font-size: 25.5px; }
  .back-tagline { left: 0; width: 312px; top: 78px; color: #fff; font-size: 10px; line-height: 14px; }
  .back-welcome { left: 0; width: 312px; text-align: center; top: 304px; color: #fff; }
  .back-address { left: 0; width: 312px; text-align: center; top: 321px; color: #fff; font-size: 10.8px; }
  .back-phone { left: 0; width: 312px; justify-content: center; top: 348px; font-size: 19px; }
</style>
</head>
<body>

<section class="card card--front" aria-label="Postcard front">
  <svg class="shapes" width="557" height="432" viewBox="0 0 557 432">
    <defs>
      <clipPath id="front-clip"><rect width="557" height="432"/></clipPath>
      <linearGradient id="couple-tone" x1="0" y1="0" x2="1" y2="1">
        <stop offset="0" stop-color="#ece8e3"/>
        <stop offset="1" stop-color="#c8b6a4"/>
      </linearGradient>
    </defs>
    <polygon points="0,0 145,0 192,100 0,100" fill="var(--taupe)"/>
    <polygon points="160,0 557,0 557,95 205,95" fill="var(--teal)"/>
    <rect x="205" y="97" width="352" height="4" fill="var(--taupe)"/>
    <rect x="250" y="375" width="307" height="3" fill="var(--teal-light)"/>
    <rect x="250" y="378" width="307" height="54" fill="var(--taupe)"/>
    <g clip-path="url(#front-clip)">
      <circle cx="90" cy="320" r="242" fill="var(--teal-light)"/>
      <circle cx="90" cy="320" r="236" fill="#fff"/>
      <circle cx="90" cy="320" r="233" fill="url(#couple-tone)" role="img" aria-label="Photo of a smiling senior couple embracing"/>
    </g>
  </svg>

  <div class="txt hours">
    <div class="head">HOURS</div>
    <div>Mon - Thru -Thurs</div>
    <div>9:00am - 5:00pm</div>
    <div class="small">(closed for lunch 12:00pm - 1:00pm.)</div>
    <div>Fri open 9:00am - 1:00pm</div>
  </div>

  <h1 class="txt title front-title">Bluebonnet Hearing<br>Aid Device Center</h1>
  <p class="txt tagline front-tagline">Family Owned &amp; Servicing<br>The Big Country for Over 30 Years</p>
  <p class="txt service">Hearing Aid Sales &amp; Service</p>
  <p class="txt free">FREE HEARING TEST. FRESH BATTERIES</p>

  <div class="offer offer--batteries">
    <div class="label">FRESH BATTERIES</div>
    <div class="deal">Buy one 50% off<br>on 2nd pack</div>
    <div class="note">LIMITED TIME</div>
  </div>
  <div class="offer offer--discounts">
    <div class="label">THIS MONTH ONLY</div>
    <div class="deal">Special discounts</div>
    <div class="note">on new state of the art<br>hearing aids w/remote</div>
  </div>

  <p class="txt welcome front-welcome">Walk-in welcome Appointments appreciated!</p>
  <p class="txt front-address">417 Marwick Ln Abilene Texas 79488</p>
  <p class="txt phone front-phone">
    <svg width="13" height="15" viewBox="0 0 24 24" aria-hidden="true"><path d="M6.6 10.8c1.4 2.8 3.8 5.1 6.6 6.6l2.2-2.2c.3-.3.7-.4 1-.2 1.1.4 2.3.6 3.6.6.6 0 1 .4 1 1V20c0 .6-.4 1-1 1C10.6 21 3 13.4 3 4c0-.6.4-1 1-1h3.5c.6 0 1 .4 1 1 0 1.3.2 2.5.6 3.6.1.3 0 .7-.2 1z"/></svg>
    325-555-0147
  </p>
</section>

<section class="card card--back" aria-label="Postcard back">
  <svg class="shapes" width="557" height="432" viewBox="0 0 557 432">
    <defs>
      <linearGradient id="fitting-tone" x1="0" y1="0" x2="1" y2="1">
        <stop offset="0" stop-color="#d9762f"/>
        <stop offset=".55" stop-color="#e3c3a0"/>
        <stop offset="1" stop-color="#3f5f95"/>
      </linearGradient>
    </defs>
    <rect x="0" y="0" width="312" height="112" fill="var(--teal)"/>
    <rect x="2" y="117" width="310" height="175" fill="url(#fitting-tone)" role="img" aria-label="Photo of a woman choosing a hearing aid from a tray"/>
    <rect x="0" y="296" width="312" height="89" fill="var(--taupe)"/>
    <rect x="476" y="22" width="67" height="48" fill="none" stroke="var(--rule)" stroke-width="1"/>
    <g stroke="var(--rule)" stroke-width="1">
      <line x1="337" y1="158" x2="543" y2="158"/>
      <line x1="337" y1="182" x2="543" y2="182"/>
      <line x1="337" y1="206" x2="543" y2="206"/>
      <line x1="337" y1="230" x2="543" y2="230"/>
      <line x1="337" y1="254" x2="543" y2="254"/>
    </g>
  </svg>

  <h2 class="txt title back-title">Bluebonnet Hearing<br>Aid Device Center</h2>
  <p class="txt tagline back-tagline">Family Owned &amp; Servicing<br>The Big Country for Over 30 Years</p>
  <p class="txt welcome back-welcome">Walk-in welcome Appointments appreciated!</p>
  <p class="txt back-address">417 Marwick Ln Abilene Texas 79488</p>
  <p class="txt phone back-phone">
    <svg width="13" height="15" viewBox="0 0 24 24" aria-hidden="true"><path d="M6.6 10.8c1.4 2.8 3.8 5.1 6.6 6.6l2.2-2.2c.3-.3.7-.4 1-.2 1.1.4 2.3.6 3.6.6.6 0 1 .4 1 1V20c0 .6-.4 1-1 1C10.6 21 3 13.4 3 4c0-.6.4-1 1-1h3.5c.6 0 1 .4 1 1 0 1.3.2 2.5.6 3.6.1.3 0 .7-.2 1z"/></svg>
    325-555-0147
  </p>
</section>

</body>
</html>
```